Brightfield Optics seeks updated contemporary business card

Brightfield Optics utilizes advanced technology and we take pride in the modern look and feel of our practice. We like our current card, but it's been four years so it is time for an update.

Target Market(s)

Females 25-45 make the most health care decisions for their family.

Contact Information for Business Card

Clean front. Back with info and with empty space for appointment time or other small note

Requirements
Must have
• Logo
Meadow Costmart, 24816 E Tamsworth Ave
Pinecrest Costmart, 3084 S Dunmore Rd
Call or text: 509-482-6134
email: hello@brightfieldoptics.example
brightfieldoptics.example
Dr Tomas Bregan & Associates

```html
<!DOCTYPE html>
<html lang="en">
<head>
<meta charset="utf-8">
<title>Brightfield Optics – Business Card</title>
<link href="https://fonts.googleapis.com/css2?family=Open+Sans:wght@400;600;700&display=swap" rel="stylesheet">
<style>
  :root {
    --backdrop: #e9e9ea;
    --card: #2b2b2d;
    --card-deep: #202022;
    --pattern-light: #5a5a5e;
    --accent: #1a86d0;
    --text-light: #f2f2f2;
    --text-muted: #c9c9cc;
    --rule: #6a6a6e;
    --note-line: #55555a;
  }
  * { box-sizing: border-box; margin: 0; padding: 0; }
  html, body { width: 1200px; height: 801px; overflow: hidden; }
  body {
    background: var(--backdrop);
    font-family: "Open Sans", Arial, sans-serif;
    display: flex;
    align-items: center;
    justify-content: center;
    gap: 48px;
  }
  .card {
    position: relative;
    width: 530px;
    height: 303px;
    background: var(--card);
    border-bottom: 4px solid var(--accent);
    overflow: hidden;
  }

  /* Shared brand lockup */
  .brand-row { display: flex; align-items: center; gap: 10px; }
  .brand-dot {
    border-radius: 50%;
    background: var(--accent);
    flex: none;
  }
  .brand-name {
    color: var(--text-light);
    font-weight: 700;
    text-transform: uppercase;
    line-height: 1;
    white-space: nowrap;
  }
  .brand-tagline {
    color: var(--text-light);
    font-weight: 700;
    text-transform: uppercase;
    white-space: nowrap;
  }

  /* Info side */
  .card-info .brand {
    position: absolute;
    left: 40px;
    top: 78px;
  }
  .card-info .brand-dot { width: 24px; height: 24px; }
  .card-info .brand-name { font-size: 18px; letter-spacing: .3px; }
  .card-info .brand-tagline { font-size: 9.5px; letter-spacing: 1px; margin-top: 5px; }

  .divider {
    position: absolute;
    left: 300px; top: 62px;
    width: 1px; height: 84px;
    background: var(--rule);
  }
  .contact-list {
    position: absolute;
    left: 316px; top: 68px;
    list-style: none;
    color: var(--text-light);
    font-size: 10.5px;
    white-space: nowrap;
  }
  .contact-list li {
    display: flex; align-items: center; gap: 7px;
    margin-bottom: 9px;
  }
  .contact-list svg { width: 11px; height: 11px; flex: none; }

  .doctor {
    position: absolute;
    left: 40px; top: 172px;
  }
  .doctor-name {
    color: var(--accent);
    font-weight: 600;
    font-size: 16px;
    text-transform: uppercase;
    letter-spacing: .5px;
  }
  .doctor-role { color: var(--text-muted); font-size: 12px; }

  .addresses {
    position: absolute;
    left: 40px; top: 232px;
    color: var(--text-muted);
    font-size: 10.5px;
    line-height: 1.6;
    white-space: nowrap;
  }

  .note-space {
    position: absolute;
    left: 316px; top: 196px;
    width: 174px; height: 64px;
    border-bottom: 1px solid var(--note-line);
    background:
      linear-gradient(var(--note-line), var(--note-line)) left 31px / 100% 1px no-repeat;
  }

  /* Front side */
  .pattern-field {
    position: absolute; inset: 0;
    background: linear-gradient(120deg, var(--card-deep) 0%, var(--card) 50%, var(--pattern-light) 100%);
  }
  .front-brand {
    position: absolute;
    right: 40px; bottom: 58px;
  }
  .card-front .brand-dot { width: 30px; height: 30px; }
  .card-front .brand-name { font-size: 25px; letter-spacing: .5px; }
  .card-front .brand-tagline { font-size: 11px; letter-spacing: 1.2px; margin-top: 6px; }
</style>
</head>
<body>

  <section class="card card-info" aria-label="Card back with contact details">
    <div class="brand brand-row">
      <span class="brand-dot"></span>
      <div>
        <div class="brand-name">Brightfield Optics</div>
        <div class="brand-tagline">Advanced Eye Care</div>
      </div>
    </div>
    <div class="divider"></div>
    <ul class="contact-list">
      <li>
        <svg viewBox="0 0 12 12"><path d="M3 1 L5 3.5 L4 5 Q5 7 7 8 L8.5 7 L11 9 L9.5 11 Q4 10.5 1 3 Z" fill="var(--accent)"/></svg>
        509-482-6134
      </li>
      <li>
        <svg viewBox="0 0 12 12"><rect x="1" y="2.5" width="10" height="7" fill="none" stroke="var(--accent)" stroke-width="1.2"/><path d="M1 2.5 L6 7 L11 2.5" fill="none" stroke="var(--accent)" stroke-width="1.2"/></svg>
        hello@brightfieldoptics.example
      </li>
      <li>
        <svg viewBox="0 0 12 12"><circle cx="6" cy="6" r="5" fill="none" stroke="var(--accent)" stroke-width="1.2"/><path d="M1 6 H11 M6 1 Q3 6 6 11 M6 1 Q9 6 6 11" fill="none" stroke="var(--accent)" stroke-width="1"/></svg>
        www.brightfieldoptics.example
      </li>
    </ul>
    <div class="doctor">
      <div class="doctor-name">Dr Tomas Bregan</div>
      <div class="doctor-role">Associates</div>
    </div>
    <div class="addresses">
      <p>Meadow Costmart, 24816 E Tamsworth Ave</p>
      <p>Pinecrest Costmart, 3084 S Dunmore Rd</p>
    </div>
    <div class="note-space" aria-label="Blank space for appointment note"></div>
  </section>

  <section class="card card-front" aria-label="Card front with brand name">
    <div class="pattern-field" role="img" aria-label="Embossed repeating decorative pattern in dark greys"></div>
    <div class="front-brand brand-row">
      <span class="brand-dot"></span>
      <div>
        <div class="brand-name">Brightfield Optics</div>
        <div class="brand-tagline">Advanced Eye Care</div>
      </div>
    </div>
  </section>

</body>
</html>
```